AVOID HOT “HARISSA” SAUCE. IN CAN

Brand Overview: Create a dynamic and eye-catching label for our new hot sauce IN CAN, “DANZO.” Our brand is all about delivering a fiery flavor experience that combines the intensity of various peppers with unique, bold ingredients. The hot sauce targets spice enthusiasts who crave both heat and distinctive taste profiles.

Key Messages: Intensity: Emphasize the extreme heat level of the hot sauce to appeal to spice lovers.
Traditional: The taste is traditional
Flavor Fusion: Highlight the unique blend of peppers and special ingredients that sets DANZO

Quality Ingredients: Convey the use of premium, natural ingredients to reinforce the high-quality aspect of our product.

Versatility: Communicate the sauce's versatility – perfect for various cuisines and dishes. Design Elements:

Color Palette: Use fiery reds, oranges, and yellows to convey the heat, with accents of dark and smoky tones to suggest depth of flavor.

Typography: Choose bold and legible fonts for the product name, ensuring it is easily readable from a distance.
Imagery: Incorporate visuals of flaming peppers or a stylized fire to reinforce the spicy nature of the hot sauce.
Consider using images of the key ingredients to showcase the fusion of flavors.

Texture/Background: Add a textured or gradient background to enhance visual interest and give a sense of depth.

Label Information: Product Name Hot Sauce "HARISSA" Heat Level

Indicator: Use a visual scale or iconography to indicate the spiciness level.

Ingredients: Highlight key ingredients and emphasize their quality, peppers, water, salt
SIZE: L: 12cm H: 5.5cm

Net Weight: 140g

Regulatory Information: Ensure compliance with all relevant food labeling regulations, including ingredients list, nutritional information, and contact details.

Competitor Analysis: Examine other hot sauce labels in the market to identify design trends and differentiators.
Inspiration: Consider drawing inspiration from elements like flames, peppers, or global spice motifs to create a visually striking and memorable label. Mood/Emotion: The label should evoke excitement, daring, and a sense of adventure – capturing the thrill of experiencing the intense flavor of HARISSA DANZO Hot Sauce.

Target Audience: Spice enthusiasts, foodies, and individuals seeking a unique and bold addition to their culinary experiences.

Delivery Format: The label design should be suitable for various packaging sizes, ensuring scalability without sacrificing visual impact. Remember to balance the vibrant and intense visuals with clarity and readability and send the FONT at the moment of the delivery.

Target Market(s)

European

Font styles to use
Decorative

Colors
FFF300
FFF600
FEFA6F
FFFEC7
FFFEE8
FFC000
F8CF3A
FAE287
FDF2CF
FEFAEE
EE7325
F08F49
F5BC92
FAE3D3
FDF4ED
EB3D1F
EC4F4E
F09395
F8D3D4
FCEDEE

Requirements
Must have
• LOGO, BARCODE, Nutritional facts, INGREDIENTS

```html
<!DOCTYPE html>
<html lang="en">
<head>
<meta charset="utf-8">
<title>DANZO Hot Sauce Harissa – Can Label</title>
<link rel="stylesheet" href="https://fonts.googleapis.com/css2?family=Cinzel:wght@400;700&family=Rubik+Dirt&display=swap">
<style>
  :root {
    --page: #ffffff;
    --label-black: #140303;
    --deep-red: #3a0705;
    --fire-red: #eb3d1f;
    --band-red: #d81414;
    --gold: #f8cf3a;
    --flame-yellow: #fff300;
    --flame-orange: #ee7325;
    --pepper-green: #2f8a2a;
    --text-white: #ffffff;
    --hot-white: #fcedee;
  }
  * { box-sizing: border-box; margin: 0; padding: 0; }
  html, body {
    width: 1200px; height: 1200px; overflow: hidden;
    background: var(--page);
  }
  .canvas { position: relative; width: 1200px; height: 1200px; }

  .label {
    position: absolute; left: 50px; top: 348px;
    width: 1100px; height: 504px; overflow: hidden;
    background: radial-gradient(ellipse at 50% 60%, #7a0d08 0%, var(--deep-red) 40%, var(--label-black) 75%);
  }
  .band-top {
    position: absolute; left: 0; top: 0; width: 100%; height: 38px;
    background: var(--band-red);
    border-bottom: 3px solid var(--gold);
  }
  .band-bottom {
    position: absolute; left: 0; bottom: 0; width: 100%; height: 62px;
    background: var(--band-red);
    border-top: 3px solid var(--gold);
    display: flex; align-items: center; justify-content: center;
  }
  .net-weight {
    font-family: "Cinzel", serif; font-weight: 700;
    font-size: 26px; letter-spacing: 3px; color: var(--text-white);
  }

  .art { position: absolute; }
  .art-peppers-left {
    left: 90px; top: 70px; width: 230px; height: 370px;
    background: linear-gradient(160deg, rgba(235,61,31,0.85) 0%, rgba(160,16,10,0.7) 45%, rgba(47,138,42,0.45) 100%);
    border-radius: 40% 60% 50% 50%;
    filter: blur(2px);
  }
  .art-peppers-right {
    right: 90px; top: 60px; width: 230px; height: 380px;
    background: linear-gradient(200deg, rgba(47,138,42,0.5) 0%, rgba(235,61,31,0.85) 40%, rgba(160,16,10,0.7) 100%);
    border-radius: 60% 40% 50% 50%;
    filter: blur(2px);
  }
  .art-flame {
    left: 390px; top: 300px; width: 320px; height: 150px;
    background: radial-gradient(ellipse at 50% 60%, var(--flame-yellow) 0%, var(--flame-orange) 35%, rgba(235,61,31,0.6) 60%, rgba(235,61,31,0) 75%);
  }

  .logo {
    position: absolute; left: 0; top: 60px; width: 100%;
    display: flex; justify-content: center; align-items: center; gap: 10px;
  }
  .logo-dot { width: 14px; height: 14px; border-radius: 50%; background: var(--text-white); }
  .logo-name {
    font-family: "Cinzel", serif; font-weight: 700;
    font-size: 42px; letter-spacing: 4px; color: var(--text-white);
  }

  .title-hot {
    position: absolute; left: 0; top: 120px; width: 100%; text-align: center;
    font-family: "Rubik Dirt", system-ui, sans-serif;
    font-size: 78px; color: var(--hot-white); letter-spacing: 2px;
    text-shadow: 0 0 18px var(--fire-red), 0 0 4px var(--fire-red);
  }
  .title-harissa {
    position: absolute; left: 0; top: 200px; width: 100%; text-align: center;
    font-family: "Cinzel", serif; font-weight: 400;
    font-size: 92px; letter-spacing: 6px; color: var(--text-white);
    line-height: 1;
  }
  .claims {
    position: absolute; left: 50%; top: 305px; transform: translateX(-50%);
    width: 420px; list-style: none; text-align: center;
    font-family: "Cinzel", serif; color: var(--text-white);
    font-size: 22px; letter-spacing: 2px;
  }
  .claims li { padding: 3px 0; }
  .claims li + li { border-top: 1px solid rgba(255,255,255,0.7); }

  .heat-badge {
    position: absolute; right: 40px; top: 240px;
    width: 70px; height: 70px; border-radius: 50%;
    background: var(--flame-orange);
    display: flex; align-items: center; justify-content: center;
    font-family: "Cinzel", serif; font-weight: 700; font-size: 18px; color: var(--text-white);
  }
</style>
</head>
<body>
<div class="canvas">
  <section class="label">
    <div class="band-top"></div>

    <div class="art art-peppers-left" role="img" aria-label="Red chili peppers and coriander leaves"></div>
    <div class="art art-peppers-right" role="img" aria-label="Red and green chili peppers with coriander leaves"></div>
    <div class="art art-flame" role="img" aria-label="Flaming red chili pepper on a wooden board"></div>

    <div class="logo">
      <span class="logo-dot"></span>
      <span class="logo-name">DANZO</span>
    </div>

    <div class="title-hot">HOT SAUCE</div>
    <h1 class="title-harissa">HARISSA</h1>

    <ul class="claims">
      <li>ORIGINAL HOT SPEACY</li>
      <li>EXTREME HEAT LEVEL</li>
      <li>TRADICIONAL</li>
    </ul>

    <div class="heat-badge">HOT</div>

    <div class="band-bottom">
      <span class="net-weight">NET WEIGHT: 140G</span>
    </div>
  </section>
</div>
</body>
</html>
```